Business card for hi tech component manufacturer, specialising in after market firearms components a
Tovin Industries (Ti)
Use same font as used in my logo
Owen Petrie
General Manager
Postal: PO Box 58491, Brackley, Christchurch 8245, New Zealand
Physical: 14 Garnet Street, Fenwick, Christchurch 8024, New Zealand
sales@tovin-works.example.nz
tovin-works.example.nz
Details are to be confirmed in future. Please allow space for Addresses, Phone, Cell, Email and Web address.
Hi Quill42,
You are the winner of the stationary project for Tovin Industries.
We have had some commercial issues with the company name Tovin, and as this is a start up company, we have changed the name.
The new Company name is ZENTH Industries. I have the new logo file, how do I send this to you?
As such I have a new set of address and company name for you to change for the final design.
And the only contact details we want on all the stationary options that you supplied are as follows:
Web: www.zenth.example.nz
Email address: sales@zenth.example.nz
Phone: +6429184306
Contact: Owen Petrie General Manager
Please advise, if you require a different file type, I have .ai, .eps, .gif, .pdf, .png, .psd, .jpg, .tif
I look forward to hearing from you.
Best regards,
Owen

```html
<!DOCTYPE html>
<html lang="en">
<head>
<meta charset="utf-8">
<title>ZENTH Industries Stationery</title>
<link rel="stylesheet" href="https://fonts.googleapis.com/css2?family=Michroma&family=Open+Sans:wght@400;600&display=swap">
<style>
  :root{
    --board:#eceeef;
    --paper:#ffffff;
    --ink:#3b4a55;
    --ink-soft:#6d7a83;
    --label:#8a9399;
    --shadow:rgba(40,50,60,.14);
  }
  *{box-sizing:border-box;margin:0;padding:0}
  html,body{width:1200px;height:826px;overflow:hidden}
  body{background:var(--board);position:relative;font-family:"Open Sans",Arial,sans-serif;color:var(--ink)}
  .sheet{position:absolute;background:var(--paper);box-shadow:0 1px 4px var(--shadow)}
  .piece-label{position:absolute;font-family:"Michroma",Arial,sans-serif;font-size:6px;letter-spacing:.12em;text-transform:uppercase;color:var(--label);text-align:center}
  .brand{display:flex;align-items:center;gap:8px;font-family:"Michroma",Arial,sans-serif;color:var(--ink);text-transform:uppercase;letter-spacing:.04em;white-space:nowrap}
  .brand-square{background:var(--ink);flex:none}
  .contact-list{list-style:none;font-family:"Michroma",Arial,sans-serif;color:var(--ink-soft)}
  .contact-list li{display:flex;align-items:flex-start;gap:5px}
  .contact-list svg{flex:none;fill:none;stroke:var(--ink);stroke-width:1.4}

  /* Letterhead */
  .letterhead{left:247px;top:14px;width:569px;height:768px}
  .letterhead .brand{position:absolute;left:22px;top:30px;font-size:13px}
  .letterhead .brand-square{width:22px;height:22px}
  .letterhead .contact-list{position:absolute;left:420px;top:24px;font-size:6.5px;line-height:1.45}
  .letterhead .contact-list li{margin-bottom:5px}
  .letterhead .contact-list li.tight{margin-bottom:1px}
  .letterhead .contact-list svg{width:9px;height:9px;margin-top:1px}

  /* Business cards */
  .card{width:188px;height:108px}
  .card .brand{position:absolute;left:10px;top:12px;font-size:6.5px;gap:5px}
  .card .brand-square{width:10px;height:10px}
  .card .contact-list{position:absolute;left:12px;top:54px;font-size:3.6px;line-height:1.5}
  .card .contact-list li{margin-bottom:1.5px}
  .card .contact-list svg{width:5px;height:5px}
  .card .person{position:absolute;right:14px;bottom:16px;font-family:"Michroma",Arial,sans-serif;font-size:4.2px;line-height:1.5;text-align:right;color:var(--ink)}
  .card .person .role{color:var(--ink-soft)}

  .card-full{left:53px;top:271px}
  .card-web{left:53px;top:427px}
  .card-rear{left:878px;top:341px}
</style>
</head>
<body>

  <p class="piece-label" style="left:53px;top:238px;width:188px">Business Card with all info</p>
  <section class="sheet card card-full">
    <div class="brand"><span class="brand-square"></span>ZENTH Industries</div>
    <ul class="contact-list">
      <li><svg viewBox="0 0 10 10"><path d="M5 9.2S1.8 6 1.8 4a3.2 3.2 0 0 1 6.4 0C8.2 6 5 9.2 5 9.2z"/></svg>PO Box 58491, Brackley, Christchurch 8245</li>
      <li><svg viewBox="0 0 10 10"><path d="M5 9.2S1.8 6 1.8 4a3.2 3.2 0 0 1 6.4 0C8.2 6 5 9.2 5 9.2z"/></svg>14 Garnet Street, Fenwick, Christchurch 8024</li>
      <li><svg viewBox="0 0 10 10"><rect x="2.5" y="1" width="5" height="8" rx="1"/></svg>+64 3 555 0142</li>
      <li><svg viewBox="0 0 10 10"><rect x="2.5" y="1" width="5" height="8" rx="1"/></svg>+64 29 184 306</li>
      <li><svg viewBox="0 0 10 10"><rect x="1" y="2.5" width="8" height="5"/><path d="M1 2.5l4 3 4-3"/></svg>sales@zenth.example.nz</li>
      <li><svg viewBox="0 0 10 10"><circle cx="5" cy="5" r="4"/><path d="M1 5h8M5 1c-2 2.5-2 5.5 0 8M5 1c2 2.5 2 5.5 0 8"/></svg>www.zenth.example.nz</li>
    </ul>
    <div class="person"><p>Owen Petrie</p><p class="role">General Manager</p></div>
  </section>

  <p class="piece-label" style="left:53px;top:408px;width:188px">Business Card with email and web address only</p>
  <section class="sheet card card-web">
    <div class="brand"><span class="brand-square"></span>ZENTH Industries</div>
    <ul class="contact-list" style="top:62px">
      <li><svg viewBox="0 0 10 10"><rect x="1" y="2.5" width="8" height="5"/><path d="M1 2.5l4 3 4-3"/></svg>sales@zenth.example.nz</li>
      <li><svg viewBox="0 0 10 10"><circle cx="5" cy="5" r="4"/><path d="M1 5h8M5 1c-2 2.5-2 5.5 0 8M5 1c2 2.5 2 5.5 0 8"/></svg>www.zenth.example.nz</li>
    </ul>
  </section>

  <main class="sheet letterhead">
    <div class="brand"><span class="brand-square"></span>ZENTH Industries</div>
    <ul class="contact-list">
      <li class="tight"><svg viewBox="0 0 10 10"><path d="M5 9.2S1.8 6 1.8 4a3.2 3.2 0 0 1 6.4 0C8.2 6 5 9.2 5 9.2z"/></svg><span>PO Box 58491, Brackley, Christchurch<br>8245, New Zealand</span></li>
      <li><svg viewBox="0 0 10 10"><path d="M5 9.2S1.8 6 1.8 4a3.2 3.2 0 0 1 6.4 0C8.2 6 5 9.2 5 9.2z"/></svg><span>14 Garnet Street, Fenwick,<br>Christchurch 8024, New Zealand</span></li>
      <li class="tight"><svg viewBox="0 0 10 10"><rect x="2.5" y="1" width="5" height="8" rx="1"/></svg>+64 3 555 0142</li>
      <li class="tight"><svg viewBox="0 0 10 10"><rect x="2.5" y="1" width="5" height="8" rx="1"/></svg>+64 29 184 306</li>
      <li class="tight"><svg viewBox="0 0 10 10"><rect x="1" y="2.5" width="8" height="5"/><path d="M1 2.5l4 3 4-3"/></svg>sales@zenth.example.nz</li>
      <li><svg viewBox="0 0 10 10"><circle cx="5" cy="5" r="4"/><path d="M1 5h8M5 1c-2 2.5-2 5.5 0 8M5 1c2 2.5 2 5.5 0 8"/></svg>www.zenth.example.nz</li>
    </ul>
  </main>
  <p class="piece-label" style="left:247px;top:796px;width:569px">Letter Head</p>

  <section class="sheet card card-rear">
    <div class="brand"><span class="brand-square"></span>ZENTH Industries</div>
    <ul class="contact-list">
      <li><svg viewBox="0 0 10 10"><path d="M5 9.2S1.8 6 1.8 4a3.2 3.2 0 0 1 6.4 0C8.2 6 5 9.2 5 9.2z"/></svg>PO Box 58491, Brackley, Christchurch 8245</li>
      <li><svg viewBox="0 0 10 10"><path d="M5 9.2S1.8 6 1.8 4a3.2 3.2 0 0 1 6.4 0C8.2 6 5 9.2 5 9.2z"/></svg>14 Garnet Street, Fenwick, Christchurch 8024</li>
      <li><svg viewBox="0 0 10 10"><rect x="2.5" y="1" width="5" height="8" rx="1"/></svg>+64 29 184 306</li>
      <li><svg viewBox="0 0 10 10"><rect x="1" y="2.5" width="8" height="5"/><path d="M1 2.5l4 3 4-3"/></svg>sales@zenth.example.nz</li>
      <li><svg viewBox="0 0 10 10"><circle cx="5" cy="5" r="4"/><path d="M1 5h8M5 1c-2 2.5-2 5.5 0 8M5 1c2 2.5 2 5.5 0 8"/></svg>www.zenth.example.nz</li>
    </ul>
    <div class="person"><p>Owen Petrie</p><p class="role">General Manager</p></div>
  </section>
  <p class="piece-label" style="left:878px;top:472px;width:188px">Rear Profile</p>

</body>
</html>
```